Birchwell Hub Homepage Banner designs

We need homepage banners that reflects our market place business showing our process, using some text but mostly nice looking images, please find attached some images to help explain our process to you that should be reflected on the banner. Main banner Size: 2050x854 pixels

Please see the banner on our website, to see how it fits behind the 4 central banners http://birchwellnorthway.com/

Slider images:
#3. http://www.birchwellnorthway.com/skins/default/en/modules/QuillBadger/VelvetPlumage/images/img/item_slide1.jpg

We will be replacing the 4 central banners (we will not be replacing text or sign up icon, just the image)
The 4 central banners: Size: 570x434 pixels
#6. http://www.birchwellnorthway.com/skins/default/en/modules/QuillBadger/VelvetPlumage/images/img/banner1.jpg
#7. http://www.birchwellnorthway.com/skins/default/en/modules/QuillBadger/VelvetPlumage/images/img/banner2.jpg
#8. http://www.birchwellnorthway.com/skins/default/en/modules/QuillBadger/VelvetPlumage/images/img/banner3.jpg
#9. http://www.birchwellnorthway.com/skins/default/en/modules/QuillBadger/VelvetPlumage/images/img/banner4.jpg

Here is what is needed on those 4 banners

#1. Should show product images, representing manufacturers. (see attached product images)
#2. Should have a truck representing Distributors.
#3. Should show a store with retailer, representing retailers.
#4. Should have people, buyers, representing buying clubs, or networks of people who buy in groups.

Target Market(s)

Natural Products Industry, Supermarkets, Manufacturers, Distributors, Retailers

Industry/Entity Type

Business

Requirements
Must have
• 1. High quality Images like the ones you are replacing.
• 2. Must show our sales process (see attached banner for process)
• 3. Please notice the way the Main slider image is behind the 4 central banners, so make sure the enough of the main banner is showing.
• 4. Files must be given in: Jpeg, PNG, AI Source, GIF
Nice to have
• Show Manufacturers, Distributors, Retailers, with beautiful images.

```html
<!DOCTYPE html>
<html lang="en">
<head>
<meta charset="utf-8">
<title>Sell Manufacturers Banner</title>
<link rel="stylesheet" href="https://fonts.googleapis.com/css2?family=Great+Vibes&family=Roboto+Condensed:wght@400&display=swap">
<style>
  :root {
    --page-bg: #ffffff;
    --panel-light: #f6fbec;
    --panel-mid: #dcefc0;
    --panel-edge: #b9db8a;
    --photo-light: #e9f2dc;
    --photo-mid: #6fa23a;
    --photo-dark: #2f6a12;
    --ink: #1c1c1c;
    --order-green: #5aab1a;
    --signup-grey: #a3a3a3;
    --button-text: #ffffff;
  }
  html, body {
    margin: 0;
    padding: 0;
    width: 1200px;
    height: 914px;
    overflow: hidden;
    background: var(--page-bg);
  }
  .banner {
    position: relative;
    width: 1200px;
    height: 914px;
    overflow: hidden;
  }
  .banner-backdrop {
    position: absolute;
    inset: 0;
  }
  .product-photo {
    position: absolute;
    left: 610px;
    top: 210px;
    width: 590px;
    height: 580px;
    border-radius: 40px 0 0 40px;
    background: radial-gradient(ellipse at 45% 45%, var(--photo-light) 0%, var(--photo-mid) 55%, var(--photo-dark) 100%);
  }
  .headline {
    position: absolute;
    left: 0;
    top: 30px;
    width: 1110px;
    margin: 0;
    text-align: center;
    font-family: "Great Vibes", cursive;
    font-weight: 400;
    color: var(--ink);
    line-height: 1;
  }
  .headline-small {
    display: block;
    font-size: 72px;
    margin-right: 20px;
  }
  .headline-large {
    display: block;
    font-size: 140px;
    margin-top: -4px;
  }
  .service-list {
    position: absolute;
    left: 126px;
    top: 276px;
    margin: 0;
    white-space: nowrap;
    font-family: "Roboto Condensed", "Arial Narrow", sans-serif;
    font-size: 42px;
    line-height: 54.7px;
    color: var(--ink);
  }
  .btn {
    position: absolute;
    display: flex;
    align-items: center;
    justify-content: center;
    font-family: "Roboto Condensed", "Arial Narrow", sans-serif;
    font-size: 42px;
    color: var(--button-text);
    text-decoration: none;
  }
  .btn-order {
    left: 217px;
    top: 815px;
    width: 309px;
    height: 80px;
    background: var(--order-green);
  }
  .btn-signup {
    left: 933px;
    top: 811px;
    width: 252px;
    height: 84px;
    background: var(--signup-grey);
  }
</style>
</head>
<body>
  <main class="banner">
    <svg class="banner-backdrop" width="1200" height="914" viewBox="0 0 1200 914" aria-hidden="true">
      <defs>
        <radialGradient id="panelGlow" cx="0.45" cy="0.4" r="0.75">
          <stop offset="0" stop-color="var(--panel-light)"/>
          <stop offset="0.6" stop-color="var(--panel-mid)"/>
          <stop offset="1" stop-color="var(--panel-edge)"/>
        </radialGradient>
      </defs>
      <path d="M0,160 C0,50 80,12 210,10 L950,2 C1120,0 1200,100 1200,250 L1200,914 L130,914 C45,914 0,860 0,780 Z" fill="url(#panelGlow)"/>
    </svg>

    <div class="product-photo" role="img" aria-label="Photo of two glass jars of white natural cream with daisy flowers resting on a large green leaf"></div>

    <h1 class="headline">
      <span class="headline-small">Sell</span>
      <span class="headline-large">Manufacturers</span>
    </h1>

    <p class="service-list">We will place your product<br>with distributors and large<br>retailers, manage your<br>purchase orders,<br>mange existing<br>distributors,<br>market your<br>products.</p>

    <a class="btn btn-order" href="#">Order Now !</a>
    <a class="btn btn-signup" href="#">Sign up</a>
  </main>
</body>
</html>
```